Document Processing Services and Solutions for School Systems

I am looking to design a brochure for both Digital and Paper use. I can supply the written content. Would be looking for an overall design of the brochure with provided content worked into it.

```html
<!DOCTYPE html>
<html lang="en">
<head>
<meta charset="utf-8">
<title>Brightleaf Systems – School Document Management Brochure</title>
<link rel="stylesheet" href="https://fonts.googleapis.com/css2?family=Archivo+Black&family=Oswald:wght@500&family=Poppins:wght@400;500;600;700&family=Montserrat:wght@700&display=swap">
<style>
:root{
  --blue:#3a3a9e;
  --blue-deep:#33338f;
  --gold:#d1a215;
  --gold-deep:#c4960c;
  --grey-box:#eeeef0;
  --ink:#2a2a2a;
  --muted:#6a6a6a;
  --stage:#8f8f8f;
  --white:#ffffff;
}
*{margin:0;padding:0;box-sizing:border-box}
html,body{width:1200px;height:3035px;overflow:hidden;background:var(--stage);font-family:'Poppins',sans-serif;color:var(--ink)}
.sheet{position:absolute;left:50px;width:1100px;height:778px;background:var(--white);overflow:hidden;box-shadow:0 6px 24px rgba(0,0,0,.25)}
.sheet--outside{top:690px}
.sheet--inside{top:1528px}
.abs{position:absolute}

/* why choose us */
.why-photo{left:0;top:0;width:367px;height:313px;background:linear-gradient(160deg,#f1f1f3,#dcdce0 60%,#e9c545 61%,#e3b92c);clip-path:polygon(0 0,100% 0,100% 88%,88% 100%,0 100%)}
.why-title{left:20px;top:322px;font-family:'Archivo Black',sans-serif;font-size:25px;line-height:27px;letter-spacing:.5px;font-weight:400}
.why-title .l1{color:var(--blue)} .why-title .l2{color:var(--gold)}
.feature{position:absolute;left:18px;width:326px;height:74px;background:var(--grey-box);border-left:3px solid var(--gold-deep);box-shadow:0 3px 0 #d7d7db}
.feature-icon{position:absolute;left:7px;top:8px;width:58px;height:58px;background:var(--gold);display:flex;align-items:center;justify-content:center}
.feature-title{position:absolute;left:74px;top:8px;font-size:17px;font-weight:600;color:var(--blue)}
.feature-text{position:absolute;left:74px;top:33px;width:240px;font-size:11.5px;line-height:13px;color:var(--muted)}

/* get started */
.steps-art{left:430px;top:40px;width:280px;height:230px;background:linear-gradient(135deg,rgba(58,58,158,.14),rgba(209,162,21,.22));clip-path:polygon(55% 0,100% 0,100% 30%,30% 100%,0 100%,0 70%)}
.tag{position:absolute;left:405px;font-family:'Archivo Black',sans-serif;font-size:22px;line-height:26px;color:var(--white);padding:0 6px}
.tag--blue{background:var(--blue)} .tag--gold{background:var(--gold)}
.cta-text{font-size:12.5px;line-height:14px;color:var(--muted)}
.cta-label{left:405px;top:452px;font-family:'Montserrat',sans-serif;font-weight:700;font-size:15px;color:var(--blue)}
.cta-big{left:404px;top:468px;font-family:'Oswald',sans-serif;font-weight:500;font-size:42px;line-height:48px;color:var(--gold);white-space:nowrap}
.contact-box{left:367px;top:548px;width:366px;height:210px;background:var(--blue);border:6px solid var(--blue-deep);padding:30px 0 0 34px}
.contact-box::after{content:"";position:absolute;inset:4px;border:1px solid #5d5dbd;pointer-events:none}
.contact-row{display:flex;align-items:center;gap:10px;height:48px;color:var(--white);font-size:20px;font-weight:500}
.contact-ico{width:28px;height:28px;background:var(--gold);border-radius:3px;display:flex;align-items:center;justify-content:center;flex:none}

/* cover */
.cover-band{left:733px;top:0;width:367px;height:290px;background:var(--blue)}
.brand{left:733px;top:34px;width:367px;text-align:center;color:var(--white)}
.brand-name{font-weight:600;font-size:38px;line-height:44px}
.brand-sub{font-size:12px;letter-spacing:4px;margin-top:6px;font-weight:500}
.cover-photo{left:760px;top:150px;width:320px;height:252px;background:linear-gradient(150deg,#cfd6dc,#7c8c96 45%,#b45f4d 75%,#e27b66);border:4px solid #c9c9d6}
.cover-kicker{left:763px;top:418px;font-size:15px;font-weight:500;color:#333;letter-spacing:.5px}
.cover-head{left:762px;top:437px;font-family:'Archivo Black',sans-serif;font-size:31px;line-height:32px;font-weight:400}
.cover-head .b{color:var(--blue)} .cover-head .g{color:var(--gold)}
.cover-sub{left:763px;top:538px;font-family:'Montserrat',sans-serif;font-weight:700;font-size:11.5px;color:var(--blue)}
.pill-bar{left:763px;top:560px;width:312px;height:28px;background:var(--blue);display:flex;justify-content:space-around;align-items:center;color:#fff;font-family:'Montserrat',sans-serif;font-weight:700;font-size:13px}
.pill-bar span+span{border-left:2px solid #fff;padding-left:12px}
.cover-body{left:763px;top:600px;width:312px;font-size:12px;line-height:15.5px;color:var(--muted)}
.url-btn{left:763px;top:712px;width:306px;height:28px;background:var(--gold);color:#fff;text-align:center;font-size:15px;font-weight:500;line-height:28px;box-shadow:4px 4px 0 #e8d7a1}

/* inside */
.services-title{left:20px;top:14px;font-family:'Archivo Black',sans-serif;font-size:46px;line-height:46px;font-weight:400}
.services-title .b{color:var(--blue)} .services-title .g{color:var(--gold)}
.title-rule{left:20px;top:112px;width:320px;height:2px;background:var(--gold)}
.corner{right:0;top:0;width:190px;height:190px;background:linear-gradient(225deg,var(--gold) 0 50%,transparent 50%)}
.corner-line{right:160px;top:0;width:190px;height:18px;border-right:1px solid #bbb;border-bottom:1px solid #bbb}
.col{position:absolute;top:140px;width:325px}
.col-head{display:flex;align-items:center;gap:18px;height:84px;border-bottom:2px solid #ddd}
.col-head-ico{width:56px;height:56px;border:2px solid var(--blue);display:flex;align-items:center;justify-content:center;flex:none}
.col-title{font-weight:700;font-size:23px;line-height:24px}
.col-title .b{color:#222;display:block} .col-title .g{color:var(--blue);display:block}
.item{position:relative;height:72px;margin-top:31px;background:var(--grey-box);border-left:3px solid var(--gold-deep);border-right:3px solid var(--gold-deep);display:flex;align-items:center}
.item-ico{width:64px;display:flex;justify-content:center;flex:none}
.item-text{font-size:12.5px;line-height:14.5px;color:#333;width:240px}
.strip{position:absolute;top:590px;height:188px;width:360px}
.strip-1{left:0;background:linear-gradient(135deg,#b8b5ad,#e5e3de 55%,#9a958a)}
.strip-2{left:370px;background:linear-gradient(180deg,#3d4147,#575c62 55%,#e9e9e9)}
.strip-3{left:740px;background:linear-gradient(160deg,#7c5b44,#d8d4cb 50%,#6d6a66)}
.strip-rule{position:absolute;top:586px;left:0;width:1100px;height:3px;background:var(--gold)}
</style>
</head>
<body>

<section class="sheet sheet--outside" aria-label="Brochure outside spread">
  <div class="abs why-photo" role="img" aria-label="Photo of a puzzled woman in a yellow jacket shrugging"></div>
  <h2 class="abs why-title"><span class="l1">WHY</span><br><span class="l2">CHOOSE US?</span></h2>

  <div class="feature" style="top:388px">
    <div class="feature-icon"><svg width="34" height="30" viewBox="0 0 34 30" fill="#fff"><rect x="2" y="18" width="5" height="10"/><rect x="10" y="13" width="5" height="15"/><rect x="18" y="8" width="5" height="20"/><path d="M4 12 L14 6 L22 8 L30 2" stroke="#fff" stroke-width="2.5" fill="none"/></svg></div>
    <div class="feature-title">Increased Efficiency</div>
    <div class="feature-text">Save time with digital workflows and instant document retrieval.</div>
  </div>
  <div class="feature" style="top:474px">
    <div class="feature-icon"><svg width="32" height="36" viewBox="0 0 32 36"><path d="M16 2 L29 7 V18 C29 26 23 31 16 34 C9 31 3 26 3 18 V7 Z" fill="none" stroke="#fff" stroke-width="2.5"/><path d="M10 18 L14.5 22.5 L22 14" stroke="#fff" stroke-width="3" fill="none"/></svg></div>
    <div class="feature-title">Enhanced Security</div>
    <div class="feature-text">Protect sensitive student and faculty information.</div>
  </div>
  <div class="feature" style="top:560px">
    <div class="feature-icon"><svg width="34" height="34" viewBox="0 0 34 34"><circle cx="20" cy="11" r="8" fill="none" stroke="#fff" stroke-width="2.5"/><path d="M2 24 H12 L20 27 L31 22 V26 L20 32 L2 30 Z" fill="#fff"/></svg></div>
    <div class="feature-title">Cost Savings</div>
    <div class="feature-text">Reduce paper, printing, and storage costs.</div>
  </div>
  <div class="feature" style="top:646px">
    <div class="feature-icon"><svg width="34" height="34" viewBox="0 0 34 34"><circle cx="17" cy="17" r="14" fill="none" stroke="#fff" stroke-width="2.5"/><path d="M9 22 C9 12 17 9 25 10 C25 19 19 24 9 22 Z" fill="#fff"/></svg></div>
    <div class="feature-title">Eco-Friendly</div>
    <div class="feature-text">Minimize your school's carbon footprint by going digital.</div>
  </div>

  <div class="abs steps-art" role="img" aria-label="Decorative blue and gold stepped squares rising diagonally"></div>
  <div class="tag tag--blue" style="top:300px">GET</div>
  <div class="tag tag--gold" style="top:330px">STARTED</div>
  <div class="tag tag--blue" style="top:360px">TODAY!</div>
  <p class="abs cta-text" style="left:405px;top:396px;width:300px">Let us help you modernize your document processing system.</p>
  <p class="abs cta-label">CONTACT US FOR</p>
  <p class="abs cta-big">FREE CONSULTATION</p>
  <p class="abs cta-text" style="left:405px;top:516px;width:300px">and discover how our solutions can transform your school's document management.</p>

  <div class="abs contact-box">
    <div class="contact-row"><span class="contact-ico"><svg width="16" height="16" viewBox="0 0 16 16"><path d="M3 1 L6 1 L7 5 L5 6.5 C6 9 7 10 9.5 11 L11 9 L15 10 L15 13 C15 14 14 15 13 15 C6 15 1 10 1 3 C1 2 2 1 3 1 Z" fill="#fff"/></svg></span>555-014-2202</div>
    <div class="contact-row"><span class="contact-ico"><svg width="18" height="14" viewBox="0 0 18 14"><rect x="1" y="1" width="16" height="12" fill="none" stroke="#fff" stroke-width="1.8"/><path d="M1 1 L9 8 L17 1" stroke="#fff" stroke-width="1.8" fill="none"/></svg></span>info@brightleafdocs.com</div>
    <div class="contact-row"><span class="contact-ico"><svg width="18" height="18" viewBox="0 0 18 18" fill="none" stroke="#fff" stroke-width="1.5"><circle cx="9" cy="9" r="7.5"/><ellipse cx="9" cy="9" rx="3.2" ry="7.5"/><path d="M1.5 9 H16.5 M3 5 H15 M3 13 H15"/></svg></span>www.brightleafdocs.com</div>
  </div>

  <div class="abs cover-band"></div>
  <div class="abs brand">
    <div class="brand-name">Brightleaf</div>
    <div class="brand-sub">SYSTEMS INC</div>
  </div>
  <div class="abs cover-photo" role="img" aria-label="Photo of two women reviewing documents at a computer in an office"></div>
  <p class="abs cover-kicker">TRANSFORM YOUR</p>
  <h1 class="abs cover-head"><span class="b">SCHOOL'S</span><br><span class="g">DOCUMENT</span><br><span class="b">MANAGEMENT</span></h1>
  <p class="abs cover-sub">WITH OUR COMPREHENSIVE SOLUTIONS</p>
  <div class="abs pill-bar"><span>STREAMLINE</span><span>SECURE</span><span>SIMPLIFY</span></div>
  <p class="abs cover-body">Managing school documents efficiently is crucial for smooth operations, compliance, and productivity. Our document processing services provide innovative solutions tailored for educational institutions, ensuring secure and seamless document and data handling.</p>
  <div class="abs url-btn">www.brightleafdocs.com</div>
</section>

<section class="sheet sheet--inside" aria-label="Brochure inside spread">
  <div class="abs corner-line"></div>
  <div class="abs corner"></div>
  <h2 class="abs services-title"><span class="b">OUR</span><br><span class="g">SERVICES</span></h2>
  <div class="abs title-rule"></div>

  <div class="col" style="left:20px">
    <div class="col-head">
      <div class="col-head-ico"><svg width="30" height="30" viewBox="0 0 30 30" fill="var(--blue)"><rect x="7" y="3" width="16" height="10"/><rect x="3" y="14" width="24" height="4"/><rect x="7" y="19" width="16" height="8"/></svg></div>
      <div class="col-title"><span class="b">Document</span><span class="g">Scanning &amp;</span><span class="g">Conversion</span></div>
    </div>
    <div class="item"><div class="item-ico"><svg width="34" height="28" viewBox="0 0 34 28" fill="var(--blue)"><path d="M2 6 H12 L15 9 H32 V26 H2 Z"/></svg></div><div class="item-text">Convert paper records into digital formats for easy access and storage.</div></div>
    <div class="item"><div class="item-ico"><svg width="32" height="30" viewBox="0 0 32 30" fill="none" stroke="var(--blue)" stroke-width="3"><path d="M2 9 V2 H9 M23 2 H30 V9 M30 21 V28 H23 M9 28 H2 V21"/><path d="M6 15 H26"/></svg></div><div class="item-text">High-speed scanning for student records, administrative files, and historical archives.</div></div>
    <div class="item"><div class="item-ico"><svg width="32" height="32" viewBox="0 0 32 32"><rect x="3" y="2" width="26" height="28" fill="var(--blue)"/><rect x="6" y="16" width="20" height="10" fill="#fff"/><text x="16" y="24.5" font-size="8" font-family="Poppins" text-anchor="middle" fill="var(--blue)">OCR</text></svg></div><div class="item-text">OCR (Optical Character Recognition) for searchable and editable documents.</div></div>
  </div>

  <div class="col" style="left:387px">
    <div class="col-head">
      <div class="col-head-ico"><svg width="30" height="30" viewBox="0 0 30 30" fill="var(--blue)"><rect x="4" y="3" width="8" height="8"/><rect x="18" y="3" width="8" height="8"/><circle cx="15" cy="20" r="7"/></svg></div>
      <div class="col-title"><span class="b">Cloud-Based</span><span class="g">Document</span><span class="g">Management</span></div>
    </div>
    <div class="item"><div class="item-ico"><svg width="30" height="34" viewBox="0 0 30 34"><rect x="3" y="2" width="18" height="26" fill="var(--blue)"/><path d="M22 18 L28 20 V25 C28 29 25 31 22 32 C19 31 16 29 16 25 V20 Z" fill="var(--blue)" stroke="#fff" stroke-width="1.5"/></svg></div><div class="item-text">Secure, centralized document storage accessible from anywhere.</div></div>
    <div class="item"><div class="item-ico"><svg width="34" height="32" viewBox="0 0 34 32"><path d="M4 8 A7 7 0 0 1 18 8 V12" fill="none" stroke="var(--blue)" stroke-width="3"/><rect x="2" y="12" width="18" height="16" fill="var(--blue)"/><circle cx="26" cy="18" r="4" fill="var(--blue)"/><path d="M19 31 C19 25 33 25 33 31 Z" fill="var(--blue)"/></svg></div><div class="item-text">Role-based access controls for administrators, teachers, and staff.</div></div>
    <div class="item"><div class="item-ico"><svg width="32" height="32" viewBox="0 0 32 32" fill="var(--blue)"><ellipse cx="13" cy="6" rx="11" ry="4"/><rect x="2" y="9" width="22" height="6" rx="2"/><rect x="2" y="17" width="22" height="6" rx="2"/><rect x="2" y="25" width="22" height="6" rx="2"/><circle cx="26" cy="8" r="5" fill="none" stroke="var(--blue)" stroke-width="2.5"/></svg></div><div class="item-text">Automated backups and compliance with educational data security standards.</div></div>
  </div>

  <div class="col" style="left:754px">
    <div class="col-head">
      <div class="col-head-ico"><svg width="30" height="30" viewBox="0 0 30 30" fill="none" stroke="var(--blue)" stroke-width="2.5"><circle cx="15" cy="15" r="6"/><circle cx="15" cy="15" r="11" stroke-dasharray="4 3"/></svg></div>
      <div class="col-title"><span class="b">Workflow</span><span class="g">Automation</span></div>
    </div>
    <div class="item"><div class="item-ico"><svg width="32" height="32" viewBox="0 0 32 32"><rect x="10" y="2" width="18" height="24" fill="var(--blue)"/><circle cx="10" cy="22" r="7" fill="var(--blue)" stroke="#fff" stroke-width="2"/><circle cx="10" cy="22" r="2.5" fill="#fff"/></svg></div><div class="item-text">Digitize and streamline approval processes for enrollment, transcripts, and HR forms.</div></div>
    <div class="item"><div class="item-ico"><svg width="30" height="32" viewBox="0 0 30 32"><rect x="3" y="2" width="22" height="28" fill="var(--blue)"/><path d="M8 24 L22 8" stroke="#fff" stroke-width="3"/></svg></div><div class="item-text">Reduce paperwork and improve efficiency with automated workflows.</div></div>
    <div class="item"><div class="item-ico"><svg width="34" height="32" viewBox="0 0 34 32" fill="var(--blue)"><circle cx="10" cy="10" r="6"/><circle cx="24" cy="8" r="4"/><path d="M6 30 C6 20 28 20 28 30 Z"/></svg></div><div class="item-text">Integration capable with existing school management systems.</div></div>
  </div>

  <div class="strip-rule"></div>
  <div class="strip strip-1" role="img" aria-label="Photo of hands sorting a stack of paper records"></div>
  <div class="strip strip-2" role="img" aria-label="Photo of a woman holding a white cloud-shaped sign"></div>
  <div class="strip strip-3" role="img" aria-label="Photo of a bright open-plan office with brick walls"></div>
</section>

</body>
</html>
```